SloPitch Ad

Looking for a creative eye-catching ad to go on the front page of my website to promote a softball league. Ad dimensions needs to be 1194 by 624, or in that ratio so that it can also be used on facebook.
I have attached some graphics that I have seen on other sites that I like for general ideas. Will need the colors to match with my website (www.pkvathletics.com) but logo is not necessary

```html
<!DOCTYPE html>
<html lang="en">
<head>
<meta charset="UTF-8">
<title>Softball Leagues Now Open</title>
<link rel="stylesheet" href="https://fonts.googleapis.com/css2?family=Arvo:wght@700&family=Oswald:wght@600&display=swap">
<style>
  :root {
    --backdrop: #8a8a8a;
    --orange: #e8470f;
    --orange-light: #f26a26;
    --orange-dark: #b8300a;
    --night: #1c1f22;
    --night-soft: #3a3f44;
    --turf: #3f8a22;
    --turf-dark: #1f4f12;
    --panel-green: #5b9a2c;
    --panel-green-light: #74b53b;
    --white: #ffffff;
    --ink: #222222;
    --jersey: #2f6f96;
    --jersey-dark: #14324a;
  }
  * { margin: 0; padding: 0; box-sizing: border-box; }
  html, body {
    width: 1200px;
    height: 671px;
    overflow: hidden;
    background: var(--backdrop);
  }
  .ad {
    position: absolute;
    left: 20px;
    top: 31px;
    width: 1160px;
    height: 609px;
    overflow: hidden;
    background: var(--night);
  }
  .stadium {
    position: absolute;
    inset: 0;
    background:
      linear-gradient(to bottom,
        var(--night-soft) 0%,
        var(--night) 55%,
        var(--turf-dark) 62%,
        var(--turf) 80%,
        var(--turf-dark) 100%);
  }
  .sunburst {
    position: absolute;
    left: 0;
    top: 0;
    width: 1160px;
    height: 240px;
  }
  .player {
    position: absolute;
    left: 40px;
    top: 20px;
    width: 360px;
    height: 589px;
    border-radius: 120px 120px 0 0;
    background: linear-gradient(to bottom, var(--jersey) 0%, var(--jersey-dark) 100%);
    opacity: 0.9;
  }
  .headline-panel {
    position: absolute;
    left: 796px;
    top: 20px;
    width: 340px;
    height: 415px;
    border-radius: 6px 6px 18px 18px;
    background: linear-gradient(to bottom, var(--panel-green-light), var(--panel-green));
    box-shadow: 0 4px 10px rgba(0,0,0,0.45);
    display: flex;
    flex-direction: column;
    align-items: center;
    justify-content: center;
    gap: 6px;
    font-family: "Arvo", serif;
    font-weight: 700;
    font-size: 84px;
    line-height: 1.08;
    color: var(--white);
    text-shadow: 2px 3px 3px rgba(0,0,0,0.45);
  }
  .headline-panel .accent { color: var(--orange); }
  .league-strip {
    position: absolute;
    left: 297px;
    top: 486px;
    width: 863px;
    height: 91px;
    background: linear-gradient(to right, rgba(255,255,255,0.2) 0%, var(--white) 12%, var(--white) 100%);
    display: flex;
    align-items: center;
    justify-content: flex-end;
    padding-right: 44px;
  }
  .league-strip h2 {
    font-family: "Oswald", sans-serif;
    font-weight: 600;
    font-size: 60px;
    letter-spacing: 0.5px;
    color: var(--ink);
    text-transform: uppercase;
  }
</style>
</head>
<body>
  <main class="ad">
    <div class="stadium" role="img" aria-label="Night stadium with floodlights above a green playing field"></div>

    <svg class="sunburst" viewBox="0 0 1160 240" aria-hidden="true">
      <defs>
        <radialGradient id="burst" cx="0.5" cy="0" r="0.8">
          <stop offset="0" stop-color="var(--orange-light)"/>
          <stop offset="1" stop-color="var(--orange)"/>
        </radialGradient>
        <clipPath id="wave">
          <path d="M0 0 H1160 V70 C1000 80 860 95 760 118 C600 160 470 205 300 200 C180 196 80 160 0 125 Z"/>
        </clipPath>
      </defs>
      <path d="M0 120 C80 160 180 210 300 214 C470 220 600 175 760 132 C860 108 1000 92 1160 84 V70 C1000 80 860 95 760 118 C600 160 470 205 300 200 C180 196 80 160 0 125 Z" fill="var(--orange-dark)"/>
      <g clip-path="url(#wave)">
        <rect width="1160" height="240" fill="url(#burst)"/>
        <g fill="var(--orange-light)" opacity="0.55">
          <path d="M580 -40 L0 0 L0 60 Z"/>
          <path d="M580 -40 L120 240 L260 240 Z"/>
          <path d="M580 -40 L400 240 L500 240 Z"/>
          <path d="M580 -40 L640 240 L740 240 Z"/>
          <path d="M580 -40 L880 240 L1010 240 Z"/>
          <path d="M580 -40 L1160 120 L1160 220 Z"/>
          <path d="M580 -40 L1160 -10 L1160 40 Z"/>
        </g>
      </g>
    </svg>

    <div class="player" role="img" aria-label="Player in blue jersey and helmet holding a stick"></div>

    <h1 class="headline-panel">
      <span>LETS</span>
      <span>PLAY</span>
      <span class="accent">BALL</span>
    </h1>

    <div class="league-strip">
      <h2>Softball Leagues Now Open</h2>
    </div>
  </main>
</body>
</html>
```